Creative Card Game Card Design for a Unique Universe

We are designing a physical card game whose closest cousin is "Runes of the Hollow" (http://www.glimmerforge.example/Runes). We are in need of a CREATIVE design for the cards that is similar, but different and unique, compared to other card games. Card designs should fit within the fantasy realm, but ultimately be portable to other genres, such as science fiction or medieval.

The fundamentals of our cards include:
• Title (up to ~3 long-ish words)
• Card type icon (attack, defend, augmented attack, augmented defend)
• Image (majority of the card)
• Instructional text area 1 (up to ~25 words)
• Instructional text area 2 (up to ~30 words)
• Copyright area
• Game logo area

The back of the card identifies each type of card with a different background with the game logo and title in front of it (probably white). Current ideas for backgrounds identifying the different types of cards are fiery red, metallic silver, marble green, and brown leather, so feel free to suggest textures for those as well.

Areas where we are looking for creativity:
• Textures and backgrounds (e.g. we like the parchment/antique paper look)
• Interesting use of transparency and/or gradient colors
• Shape and positioning of elements (but still needs to be functional)
• Overlapping of elements
• Card borders (if they make sense in your design)
• Icon style
• Fonts (we use "Lindsay EF" in our manual)
• Card size (but still needs to be usable in the player's hand; standard size is ~2.5" x 3.5")
• Card shape (but still needs to be usable in the player's hand; e.g. Rectangular but with a rounded corner)

Restrictions on the design:
• Design should be in color
• Card shape can be creative (but not too "out there"), but should be a reasonable cost to print
• First priority is to print, but cards will also be used in an SlatePad app

Tools:
• We would prefer the design was submitted in Adobe Illustrator format (vector-based)

We will give extra attention to designs that are truly unique and that we haven't seen before!

For examples of Runes cards, see http://www.glimmerforge.example/runes/tcg/article.aspx?x=roh/tcg/runes2013/cig

Thank you!
Updates

Hi there,

Appreciate you thinking about our little card design project! Just wanted to provide an update that I uploaded another file (a logo) on request, and also updated the comments with some sample text for a card, also on request.

Thanks,

Oliver.

Reason: Our small team isn't meeting until Wed to discuss the designs, so extending until we've had a chance to discuss the designs. Thanks, Oliver.

Target Market(s)

Teenagers+, English-speaking to start

Industry/Entity Type

Games

Font styles to use
Other font styles liked:
• Lindsay EF

Colors

Designer to choose colors to be used in the design.

Requirements
Should not have
• An identical look to other card games, like Runes.

```html
<!DOCTYPE html>
<html lang="en">
<head>
<meta charset="utf-8">
<title>Hollowmark Card Designs</title>
<link rel="stylesheet" href="https://fonts.googleapis.com/css2?family=Courier+Prime&family=Uncial+Antiqua&family=Roboto+Condensed:wght@400&display=swap">
<style>
  :root {
    --parchment-light: #e0a24e;
    --parchment-mid: #c9822f;
    --parchment-dark: #9a5a1c;
    --ink: #141210;
    --metal-dark: #2d3033;
    --metal-mid: #5d6264;
    --slate-paper: #c9ccc2;
    --slate-ink: #2a2c2b;
    --night-top: #7d93a3;
    --night-bottom: #1e2226;
    --oval-text: #d8d6cf;
    --badge-face: #d9d5c8;
    --gold-frame: #6b5532;
    --aged-paper: #ddd4bd;
    --rune-red: #9b2a26;
    --rune-green: #52743a;
    --rune-blue: #3f6f86;
    --rune-gold: #b08a1f;
    --back-leather: #c98a3e;
  }
  * { box-sizing: border-box; margin: 0; padding: 0; }
  html, body { width: 1200px; height: 1116px; overflow: hidden; }
  body {
    position: relative;
    background: radial-gradient(ellipse at 50% 45%, var(--parchment-light) 0%, var(--parchment-mid) 60%, var(--parchment-dark) 100%);
    font-family: "Roboto Condensed", sans-serif;
  }
  h2 { font-weight: 400; }
  .card {
    position: absolute;
    top: 80px;
    width: 306px;
    height: 472px;
    background: var(--ink);
    padding: 8px;
  }
  .copyright {
    position: absolute;
    font-family: "Roboto Condensed", sans-serif;
    font-size: 12px;
    color: var(--ink);
    white-space: nowrap;
  }
  .mark-dot {
    position: absolute;
    width: 30px; height: 30px;
    border: 2px solid var(--ink);
    border-radius: 50%;
  }

  /* Travel card */
  .card--travel { left: 70px; }
  .card--travel .frame {
    position: absolute; inset: 8px;
    background: linear-gradient(135deg, var(--metal-mid), var(--metal-dark));
  }
  .card--travel .title-plate {
    position: absolute; left: 22px; top: 20px; width: 263px; height: 48px;
    background: var(--slate-paper);
    border: 3px solid var(--metal-dark);
    font-family: "Courier Prime", monospace;
    font-size: 18px; letter-spacing: 1px;
    color: var(--slate-ink);
    display: flex; align-items: center; justify-content: center;
  }
  .card--travel .stat {
    position: absolute; left: 26px; width: 44px; height: 44px;
    border-radius: 50%;
    background: #1b1c1d;
    border: 2px solid #777b7c;
    color: #e6e6e6;
    font-family: "Courier Prime", monospace; font-size: 17px;
    display: flex; align-items: center; justify-content: center;
  }
  .card--travel .art {
    position: absolute; left: 78px; top: 78px; width: 207px; height: 158px;
    background: linear-gradient(180deg, #6b6776 0%, #b9b5c4 55%, #3c3a40 100%);
  }
  .card--travel .text-panel {
    position: absolute; left: 22px; top: 248px; width: 263px; height: 200px;
    background: var(--slate-paper);
    border: 3px solid var(--metal-dark);
    padding: 22px 11px 0 16px;
    font-family: "Courier Prime", monospace;
    font-size: 16px; line-height: 19px;
    color: var(--slate-ink);
  }
  .card--travel .text-panel p + p { margin-top: 19px; }

  /* Bonus card */
  .card--bonus { left: 447px; }
  .card--bonus .frame {
    position: absolute; inset: 8px;
    background: radial-gradient(circle at 10% 8%, #6e2a22 0%, transparent 22%),
                radial-gradient(circle at 92% 92%, #6e2a22 0%, transparent 22%),
                linear-gradient(135deg, #4a4c48, #23241f);
  }
  .card--bonus .oval {
    position: absolute; left: 18px; top: 10px; width: 272px; height: 452px;
    border-radius: 50%;
    border: 3px solid #8a7b54;
    overflow: hidden;
    background: #1a1c1e;
  }
  .card--bonus .oval-art {
    position: absolute; inset: 0 0 45% 0;
    background: linear-gradient(180deg, var(--night-top) 0%, #4b5a63 60%, var(--night-bottom) 100%);
  }
  .card--bonus .oval-title {
    position: absolute; top: 184px; width: 100%; text-align: center;
    font-family: "Uncial Antiqua", cursive; font-size: 14px;
    color: var(--oval-text);
  }
  .card--bonus .oval-text {
    position: absolute; top: 244px; left: 24px; right: 12px;
    font-family: "Uncial Antiqua", cursive; font-size: 11.5px; line-height: 17px;
    color: var(--oval-text);
    white-space: nowrap;
  }
  .card--bonus .oval-text p + p { margin-top: 17px; }
  .card--bonus .badge {
    position: absolute; width: 50px; height: 50px; border-radius: 50%;
    background: var(--badge-face); border: 3px solid #6c6452;
    font-family: "Uncial Antiqua", cursive; font-size: 24px; color: #3a352b;
    display: flex; align-items: center; justify-content: center;
  }
  .card--bonus .badge--type { left: 240px; top: 17px; }
  .card--bonus .badge--cost { left: 18px; top: 407px; }
  .card--bonus .copyright { left: 112px; top: 426px; color: #6c6a62; }
  .card--bonus .mark-dot { left: 138px; top: 375px; border-color: #55534c; }

  /* Rune card */
  .card--rune { left: 821px; }
  .card--rune .frame {
    position: absolute; inset: 8px;
    background: linear-gradient(135deg, #8a7347, var(--gold-frame) 50%, #4a3b22);
  }
  .card--rune .art {
    position: absolute; left: 24px; top: 22px; width: 260px; height: 216px;
    background: radial-gradient(ellipse at 55% 60%, #e4f4ff 0%, #7a5aa8 25%, #1c1230 55%, #050508 80%);
  }
  .card--rune .rune {
    position: absolute; width: 38px; height: 38px;
    border: 2px solid #2a2418;
    font-family: "Uncial Antiqua", cursive; font-size: 22px; color: #f1ead8;
    display: flex; align-items: center; justify-content: center;
  }
  .rune--red { left: 26px; top: 27px; background: var(--rune-red); }
  .rune--green { left: 241px; top: 27px; background: var(--rune-green); }
  .rune--blue { left: 26px; top: 197px; background: var(--rune-blue); }
  .rune--gold { left: 241px; top: 197px; background: var(--rune-gold); }
  .card--rune .text-panel {
    position: absolute; left: 24px; top: 250px; width: 260px; height: 198px;
    background: var(--aged-paper);
    border: 2px solid #3a2f1c;
    padding: 6px 8px 0 8px;
    font-family: "Uncial Antiqua", cursive; color: #2a241a;
  }
  .card--rune .panel-title { text-align: center; font-size: 14px; margin-bottom: 18px; }
  .card--rune .panel-body { font-size: 12px; line-height: 16px; }
  .card--rune .panel-body p + p { margin-top: 16px; }

  .card--travel .copyright, .card--rune .copyright { left: 154px; top: 426px; }
  .card--travel .mark-dot, .card--rune .mark-dot { left: 226px; top: 395px; }

  /* Card back */
  .card-back {
    position: absolute; left: 447px; top: 612px; width: 306px; height: 472px;
    border-radius: 14px;
    background: radial-gradient(ellipse at 50% 40%, #e3ad5e 0%, var(--back-leather) 60%, #9a6128 100%);
    display: flex; flex-direction: column; align-items: center; justify-content: center; gap: 14px;
  }
  .brand-dot {
    width: 120px; height: 120px; border-radius: 50%;
    border: 6px solid var(--ink);
    flex: none;
  }
  .brand-name {
    font-family: "Uncial Antiqua", cursive; font-size: 30px; color: var(--ink);
    white-space: nowrap;
  }
  .corner-brand {
    position: absolute; right: 28px; top: 985px;
    display: flex; align-items: center; gap: 8px;
  }
  .corner-brand .brand-dot { width: 32px; height: 32px; border-width: 3px; }
  .corner-brand .brand-name { font-size: 20px; }
</style>
</head>
<body>
  <article class="card card--travel">
    <div class="frame"></div>
    <h2 class="title-plate">Hot Air Balloon</h2>
    <div class="stat" style="top:78px">#1</div>
    <div class="stat" style="top:135px">A:5</div>
    <div class="stat" style="top:192px">X:2</div>
    <div class="art" role="img" aria-label="Hot air balloon drifting past winged beasts over a spired landscape"></div>
    <div class="text-panel">
      <p>You take a balloon to the next zone over.</p>
      <p>Player can travel up to 5x faster than his or her flying mount.</p>
    </div>
    <div class="mark-dot"></div>
    <span class="copyright">copyright©2014</span>
  </article>

  <article class="card card--bonus">
    <div class="frame"></div>
    <div class="oval">
      <div class="oval-art" role="img" aria-label="Dragon perched on a castle tower against a misty sky"></div>
      <h2 class="oval-title">Dragon's Blood</h2>
      <div class="oval-text">
        <p>All members gain +5 bonus to<br>slay the dragon.</p>
        <p>Hunters get - yet another pet.</p>
      </div>
    </div>
    <div class="badge badge--type">S</div>
    <div class="badge badge--cost">10</div>
    <div class="mark-dot"></div>
    <span class="copyright">copyright©2014</span>
  </article>

  <article class="card card--rune">
    <div class="frame"></div>
    <div class="art" role="img" aria-label="Rainbow streams of light rising from a glowing point"></div>
    <div class="rune rune--red">3</div>
    <div class="rune rune--green">8</div>
    <div class="rune rune--blue">1</div>
    <div class="rune rune--gold">4</div>
    <div class="text-panel">
      <h2 class="panel-title">Full Spectrum</h2>
      <div class="panel-body">
        <p>Grants all players 2 nights raid time with efficiency per week.</p>
        <p>Cannot be destroyed.</p>
      </div>
    </div>
    <div class="mark-dot"></div>
    <span class="copyright">copyright©2014</span>
  </article>

  <div class="card-back">
    <div class="brand-dot"></div>
    <span class="brand-name">Hollowmark</span>
  </div>

  <div class="corner-brand">
    <div class="brand-dot"></div>
    <span class="brand-name">Hollowmark</span>
  </div>
</body>
</html>
```